Website for Healthy Energy Bars

I need the layout for a website that will allow customers to purchase three different energy bars. It should have a slide show of pictures on the front page and the following tabs: About, Nutrition Info, FAQ

The website colors should not conflict with the colors of the company logo. Other than that I am open to design ideas and concepts.

Target Market(s)

Health-Conscious Eaters

Industry/Entity Type

Purchase

Number of Pages Required

3 page

Requirements
Must have
• Logo and pictures of the product
Should not have
• Colors that conflict with the logo colors

```html
<!DOCTYPE html>
<html lang="en">
<head>
<meta charset="utf-8">
<title>Leafborne – FAQ</title>
<link href="https://fonts.googleapis.com/css2?family=Arimo:wght@400;700&display=swap" rel="stylesheet">
<style>
  :root{
    --green:#6fbf1f;
    --green-dark:#3f8f10;
    --green-light:#b8e07a;
    --grey-bg:#e9e9e9;
    --grey-soft:#dedede;
    --text-grey:#6d6d6d;
    --text-dark:#3a3a3a;
    --white:#ffffff;
  }
  *{box-sizing:border-box;margin:0;padding:0}
  html,body{width:889px;height:1200px;overflow:hidden}
  body{font-family:"Arimo",Arial,sans-serif;background:var(--grey-bg);position:relative}
  .page-bg{position:absolute;inset:0;
    background:radial-gradient(ellipse at 50% 80%,var(--grey-bg) 0%,var(--grey-soft) 100%)}
  .header{position:absolute;left:0;top:0;width:889px;height:240px;background:var(--white)}
  .header-band{position:absolute;left:0;top:0;width:889px;height:240px}
  .brand{position:absolute;left:62px;top:52px;display:flex;align-items:center;gap:10px;
    font-weight:700;font-size:38px;color:var(--green-dark)}
  .brand-dot{width:34px;height:34px;border-radius:50%;background:var(--green)}
  .product-visual{position:absolute;left:478px;top:16px;width:394px;height:160px;border-radius:6px;
    background:linear-gradient(135deg,#f4f0d8,#e8dca0 55%,#c9b560)}
  .top-nav{position:absolute;right:12px;top:234px;font-size:15px;color:var(--text-dark)}
  .top-nav a{color:var(--text-dark);text-decoration:none}
  .panel{position:absolute;left:222px;top:282px;width:572px;height:755px;background:var(--white);
    box-shadow:0 0 10px rgba(0,0,0,.12)}
  .side-tabs{position:absolute;left:140px;top:290px;list-style:none}
  .side-tabs li{width:140px;height:40px;margin-bottom:6px;background:linear-gradient(#8dd13a,var(--green-dark));
    color:var(--white);font-size:21px;display:flex;align-items:center;padding-left:20px;
    clip-path:polygon(0 12%,100% 0,92% 50%,100% 100%,0 88%);box-shadow:0 2px 3px rgba(0,0,0,.2)}
  .side-tabs li.small{font-size:13px;line-height:13px}
  .faq-head{position:absolute;left:222px;width:450px;top:315px;text-align:center}
  .faq-title{font-size:36px;color:var(--green);font-weight:400}
  .faq-sub{font-size:17px;color:var(--text-grey)}
  .faq-visual{position:absolute;left:684px;top:296px;width:100px;height:142px;border-radius:8px;
    background:linear-gradient(160deg,var(--green-light),var(--green) 60%,#e4cc6a)}
  .questions{position:absolute;left:222px;width:572px;top:444px}
  .questions h2{font-size:30px;font-weight:400;color:var(--green);letter-spacing:1px;
    width:460px;text-align:center}
  .questions ol{list-style:none;margin-top:4px;padding-left:45px}
  .questions li{font-size:18px;line-height:26.5px;color:var(--green)}
  .footer-brand{position:absolute;left:566px;top:844px;display:flex;align-items:center;gap:10px;
    font-weight:700;font-size:30px;color:#8a8a8a}
  .footer-dot{width:28px;height:28px;border-radius:50%;background:#b5b5b5}
</style>
</head>
<body>
  <div class="page-bg" role="img" aria-label="Soft grey decorative background pattern"></div>

  <header class="header">
    <svg class="header-band" width="889" height="240">
      <path d="M0 150 C250 130 520 200 889 165 L889 240 L0 240 Z" fill="var(--green)"/>
      <path d="M0 170 C280 150 520 225 889 190 L889 240 L0 240 Z" fill="var(--green-dark)"/>
      <path d="M0 150 C250 130 520 200 889 165" fill="none" stroke="var(--green-light)" stroke-width="4"/>
      <rect x="0" y="226" width="889" height="14" fill="#f2f2f2"/>
    </svg>
    <div class="brand"><span class="brand-dot"></span>Leafborne</div>
    <div class="product-visual" role="img" aria-label="Product photo of three energy bar boxes"></div>
  </header>
  <nav class="top-nav"><a href="#">About</a> | <a href="#">Nutrition Info</a> | <a href="#">FAQ</a></nav>

  <main class="panel"></main>

  <ul class="side-tabs">
    <li>Home</li>
    <li>About</li>
    <li class="small">Nutrition<br>Info</li>
    <li>FAQ</li>
  </ul>

  <div class="faq-head">
    <h1 class="faq-title">FAQ</h1>
    <p class="faq-sub">Frequently Asked Questions</p>
  </div>
  <div class="faq-visual" role="img" aria-label="Question marks with an energy bar"></div>

  <section class="questions">
    <h2>QUESTIONS</h2>
    <ol>
      <li>1. What About Leafborne? What About Leafborne?</li>
      <li>2. What About Leafborne? What About Leafborne?</li>
      <li>3. What About Leafborne? What About Leafborne?</li>
      <li>4. What About Leafborne? What About Leafborne?</li>
      <li>5. What About Leafborne? What About Leafborne?</li>
      <li>6. What About Leafborne? What About Leafborne?</li>
      <li>7. What About Leafborne? What About Leafborne?</li>
      <li>8. What About Leafborne? What About Leafborne?</li>
      <li>9. What About Leafborne? What About Leafborne?</li>
      <li>10. What About Leafborne? What About Leafborne?</li>
      <li>11. What About Leafborne? What About Leafborne?</li>
      <li>12. What About Leafborne? What About Leafborne?</li>
    </ol>
  </section>

  <div class="footer-brand"><span class="footer-dot"></span>Leafborne</div>
</body>
</html>
```